A starter web site for the Ridgeway Digital Shield Association. Our target market are companies that use cyber security products and services and those who provide them.

Target Market(s)

Companies that provide cyber security products and services.

Industry/Entity Type

Security

Coding

Coded - Design and coding required

Number of Pages Required

5+ page

Font styles to use
Serif

Requirements
Must have
• We need the site to have an editor so we can add content, pictures and links to video on Clipzo.
Nice to have
• If possible a way to collect names of people interested in joining the organization. that falls into a excel spreadsheet.
Should not have
• Hard to read characters

```html
<!DOCTYPE html>
<html lang="en">
<head>
<meta charset="utf-8">
<title>Ridgeway Digital Shield Association</title>
<link href="https://fonts.googleapis.com/css2?family=Open+Sans:wght@400;600;700;800&display=swap" rel="stylesheet">
<style>
:root{
  --blue:#2a8ee0;
  --ink:#333;
  --muted:#666;
  --dark:#141414;
  --nav:#1f1f1f;
  --mist:#eeeeee;
  --white:#fff;
}
*{margin:0;padding:0;box-sizing:border-box}
html,body{width:721px;height:1200px;overflow:hidden}
body{position:relative;background:var(--white);font-family:"Open Sans",Arial,sans-serif;color:var(--ink)}
.abs{position:absolute}
.topline{left:0;top:0;width:721px;height:2px;background:var(--blue)}
.brand{left:56px;top:20px;font-weight:800;font-size:17px;line-height:17px;color:#3a3a3a;letter-spacing:.3px;text-transform:uppercase}
.search{left:405px;top:25px;width:181px;height:24px;border:1px solid #ddd;border-radius:2px;font-size:7px;color:#999;padding:7px 8px}
.search svg{position:absolute;right:6px;top:5px}
.btn{background:var(--blue);color:var(--white);font-weight:600;text-transform:uppercase;text-align:center;border-radius:2px}
.btn-member{left:597px;top:25px;width:68px;height:24px;font-size:8px;line-height:24px}
.hero{left:0;top:83px;width:721px;height:312px;background:var(--dark)}
.nav{left:56px;top:69px;width:609px;height:36px;background:var(--nav);display:flex;box-shadow:0 2px 4px rgba(0,0,0,.4)}
.nav a{color:#ddd;font-size:7.5px;text-decoration:none;text-transform:uppercase;line-height:36px;text-align:center;border-right:1px solid #333}
.nav a:last-child{border:none}
.player{left:56px;top:132px;width:413px;height:230px;border:2px solid #ccc;background:linear-gradient(135deg,#e8ecef,#9aa3ab 60%,#cdd3d8)}
.player .tools{position:absolute;right:7px;top:7px;display:flex;flex-direction:column;gap:4px}
.tool{width:33px;height:25px;background:rgba(20,20,20,.85);border-radius:2px;color:#fff;font-size:5px;font-weight:700;text-align:center;padding-top:16px}
.clipname{position:absolute;left:168px;top:110px;color:#fff;font-size:20px;font-weight:700}
.bar{position:absolute;left:6px;bottom:6px;right:6px;height:30px;display:flex;gap:5px}
.play{width:50px;height:30px;background:#1b1b1b;border-radius:2px;display:flex;align-items:center;justify-content:center}
.track{flex:1;background:#1b1b1b;border-radius:2px;position:relative}
.track .rail{position:absolute;left:6px;top:12px;width:253px;height:7px;background:#555;border:1px solid #888}
.track .fill{position:absolute;left:6px;top:12px;width:72px;height:7px;background:var(--blue)}
.track .time{position:absolute;left:65px;top:-12px;background:#fff;color:#000;font-size:7px;padding:0 3px}
.track .hd{position:absolute;right:8px;top:8px;color:var(--blue);font-size:9px;font-weight:700;font-style:italic}
.hero-title{left:490px;top:162px;color:var(--blue);font-size:17px;font-weight:600;line-height:20px}
.hero-sub{left:490px;top:184px;color:#fff;font-size:13.5px;font-weight:600;text-transform:uppercase}
.hero-text{left:492px;top:218px;width:172px;color:#ccc;font-size:7.6px;line-height:13px}
.btn-more{left:494px;top:286px;width:76px;height:27px;font-size:7.5px;line-height:27px}
.dots{left:583px;top:296px;display:flex;gap:3px}
.dots i{width:7px;height:7px;border-radius:50%;background:#444;display:block}
.dots i.on{background:var(--blue)}
.mission{left:0;top:395px;width:721px;height:174px;background:var(--mist)}
h2{font-size:13px;font-weight:400;text-transform:uppercase;color:#222}
.lead{font-size:8.6px;color:var(--muted)}
ul.points{list-style:none}
ul.points li{position:relative;padding-left:8px;font-size:7.4px;line-height:11px;color:var(--muted)}
ul.points li::before{content:"";position:absolute;left:0;top:4px;width:3px;height:3px;border-radius:50%;background:var(--blue)}
.card{top:656px;width:146px;height:180px;display:flex;align-items:flex-end;padding:0 8px 16px}
.card span{color:#fff;font-size:10.5px;line-height:16px;font-weight:600}
.arrow{top:738px}
.pitch{left:416px;top:896px;width:250px;font-size:7.4px;line-height:14.4px;color:var(--muted)}
.band{left:0;top:1094px;width:721px;height:106px;background:var(--blue)}
.footer{left:56px;top:1024px;width:609px;height:125px;background:var(--dark);display:flex;padding:20px 0 0 33px}
.footer .col h3{font-size:8px;font-weight:600;color:#fff;text-transform:uppercase;margin-bottom:6px}
.footer .col a{display:block;font-size:7px;color:#ddd;text-decoration:none;line-height:15.5px;padding-left:2px}
.social{left:56px;top:1170px;display:flex;gap:7px}
.social i{display:block;width:17px;height:17px;border-radius:50%;background:#fff}
.legal{right:56px;top:1173px;font-size:7px;color:#fff;word-spacing:1px}
</style>
</head>
<body>
<div class="abs topline"></div>
<div class="abs brand">Ridgeway Digital<br>Shield Association</div>
<div class="abs search">Enter keyword...
  <svg width="12" height="12" viewBox="0 0 12 12"><circle cx="5" cy="5" r="3.5" fill="none" stroke="#333" stroke-width="1.5"/><path d="M7.5 7.5L11 11" stroke="#333" stroke-width="2"/></svg>
</div>
<div class="abs btn btn-member">Membership</div>

<section class="abs hero"></section>
<nav class="abs nav">
  <a style="width:87px">About Us</a>
  <a style="width:171px">Membership Fees and Benefits</a>
  <a style="width:90px">Education</a>
  <a style="width:78px">Events</a>
  <a style="width:78px">Media</a>
  <a style="width:105px">Research Center</a>
</nav>

<div class="abs player">
  <div role="img" aria-label="Video still: padlock over a field of hexadecimal code" style="position:absolute;inset:0;background:radial-gradient(ellipse at 40% 45%,#6f7a85 0,#9aa4ad 35%,transparent 60%)"></div>
  <div class="clipname">Clipzo</div>
  <div class="tools">
    <div class="tool">LIKE</div><div class="tool">LATER</div><div class="tool">SHARE</div><div class="tool">EMBED</div>
  </div>
  <div class="bar">
    <div class="play"><svg width="12" height="13"><path d="M0 0L12 6.5L0 13Z" fill="#fff"/></svg></div>
    <div class="track"><div class="rail"></div><div class="fill"></div><div class="time">01:48</div><div class="hd">HD</div></div>
  </div>
</div>

<div class="abs hero-title">RIDGEWAY DIGITAL</div>
<div class="abs hero-sub">Shield Association</div>
<p class="abs hero-text">Cras congue orci at diam condimentum, in dignissim tellus elementum. Praesent id mauris eu urna vehicula rutrum sed in elit. Sed sed urna porta, viverra lacus in.</p>
<div class="abs btn btn-more">View More</div>
<div class="abs dots"><i></i><i></i><i class="on"></i><i></i></div>

<section class="abs mission">
  <h2 class="abs" style="left:56px;top:27px">Mission</h2>
  <p class="abs lead" style="left:56px;top:50px">( The Ridgeway Digital Shield Association has four purposes: )</p>
  <ul class="abs points" style="left:56px;top:74px;width:305px">
    <li>To encourage cyber security professionals to share best practices, obtain knowledge about new products/services and to constantly improve the protection of businesses located in the Commonwealth.</li>
    <li style="margin-top:20px">To be the media face for educating the public on cyber threats and defenses against hackers/cyber thieves</li>
  </ul>
  <ul class="abs points" style="left:377px;top:74px;width:290px">
    <li>To educate small business owners and the public at large about cyber security to defend companies against cyber theft of data and funds.</li>
    <li style="margin-top:31px">To education public servants about cyber security issues</li>
  </ul>
</section>

<h2 class="abs" style="left:56px;top:588px">Programming</h2>
<p class="abs lead" style="left:56px;top:610px;width:615px;line-height:14.5px">There will be different levels of programing and content focused on level of experiences and expertise.&nbsp; Programming content will be developed by working practitioners.&nbsp; The types of programing will be, but not limited to, the following:</p>

<svg class="abs arrow" style="left:36px" width="12" height="14"><path d="M10 1L3 7L10 13" fill="none" stroke="#999" stroke-width="2.5"/></svg>
<div class="abs card" style="left:56px;background:linear-gradient(180deg,#8a1e22,#3a3a3a 55%,#151515)" role="img" aria-label="Red padlock over digital code"><span>Developing and implementing cyber security plan</span></div>
<div class="abs card" style="left:210px;background:linear-gradient(180deg,#a0553f,#5a3a35 55%,#151515)" role="img" aria-label="Padlock on a circuit board"><span>New Hardware</span></div>
<div class="abs card" style="left:364px;background:linear-gradient(180deg,#7a6a52,#4a4238 55%,#151515)" role="img" aria-label="Team working at a desk with laptops"><span>New Software</span></div>
<div class="abs card" style="left:518px;background:linear-gradient(180deg,#8e9aa3,#4a5258 55%,#151515)" role="img" aria-label="Hand holding a smartphone"><span>New Phone Apps</span></div>
<svg class="abs arrow" style="left:674px" width="12" height="14"><path d="M2 1L9 7L2 13" fill="none" stroke="#999" stroke-width="2.5"/></svg>

<h2 class="abs" style="left:56px;top:864px">Benefits</h2>
<p class="abs lead" style="left:56px;top:887px">Members will receive the following benefits:</p>
<ul class="abs points" style="left:56px;top:912px;width:320px">
  <li>Product discounts</li>
  <li style="margin-top:7.5px">Research and surveys on cyber security issues</li>
  <li style="margin-top:7.5px">Private label cyber security alerts that can be sent to their clients and employees</li>
  <li style="margin-top:7.5px">Private label newsletter to be sent to clients and employees</li>
  <li style="margin-top:7.5px">Monthly conference call roundtables</li>
</ul>

<h2 class="abs" style="left:416px;top:864px">Pitch to Prospective Members</h2>
<p class="abs pitch">Cyber theft of data is growing every year.&nbsp; The Ridgeway Digital Shield Association mission is to provide information and educate members and their clients on cyber threats and ways to defend business computer systems from hackers.&nbsp; The cost of membership depends on the size of the organization ranging from individuals $149 to $5,000 for large corporate members.</p>

<div class="abs band"></div>
<footer class="abs footer">
  <div class="col" style="width:133px"><h3>Membership</h3><a>How to Join</a><a>Membership Benefits</a><a>Membership application</a></div>
  <div class="col" style="width:144px"><h3>Cyber Products</h3><a>Security Products</a><a>Security Services</a><a>Security Experts</a></div>
  <div class="col" style="width:169px"><h3>Media</h3><a>RDSA In the Media</a><a>Video Links to Cyber Security Experts</a><a>RDSA Speakers Bureau</a><a>RDSA Speaking Engagements</a></div>
  <div class="col"><h3>Industry Information</h3><a>Cyber Threats</a><a>Cyber Security Stats</a><a>Blogs</a><a>Chirpline</a></div>
</footer>
<div class="abs social"><i></i><i></i><i></i><i></i><i></i></div>
<div class="abs legal">©2014 Ridgeway Digital Shield Association. All rights reserved. &nbsp; Privacy &nbsp; Legal</div>
</body>
</html>
```